Healthcare and Professional IT Services Company need a redesigned business card

We are a IT Services company that targets small medical practices and professional business such as Attorneys, Accounts, Architects etc. We want to communicate a professional yet friendly image using recent logo redesign here on Drafthive. Like to see the colors blue and orange in the design. Must use the Tall Cedar Technology as displayed in the new logo - then also want to incorporate the fish logo as well.

Target Market(s)

Small medical and professional services

Industry/Entity Type

It Company

Contact Information for Business Card

The usual stuff, place for name address phone website. Also maybe our tagline which is "hooked on technology"

Requirements
Must have
• My new logo and the fish somewhere on the card

```html
<!DOCTYPE html>
<html lang="en">
<head>
<meta charset="utf-8">
<title>Tall Cedar Technology – Business Card</title>
<link rel="stylesheet" href="https://fonts.googleapis.com/css2?family=Open+Sans:wght@400;600&display=swap">
<style>
  :root {
    --backdrop: #2b2d31;
    --card: #ffffff;
    --brand-blue: #1d8fd6;
    --name-blue: #1c78c4;
    --ink: #1a1a1a;
    --accent-orange: #f08a3c;
    --fish-teal: #29a9c9;
    --fish-blue: #2f7fd0;
  }
  * { margin: 0; padding: 0; box-sizing: border-box; }
  html, body { width: 1200px; height: 864px; overflow: hidden; }
  body {
    background: var(--backdrop);
    font-family: "Open Sans", sans-serif;
    position: relative;
  }
  .card {
    position: absolute;
    background: var(--card);
    overflow: hidden;
    box-shadow: 0 6px 18px rgba(0,0,0,.45);
  }
  .card--front { left: 200px; top: 80px; width: 600px; height: 300px; }
  .card--back  { left: 185px; top: 400px; width: 660px; height: 330px; }

  .brand-mark {
    position: absolute;
    display: flex; align-items: center; gap: 12px;
    color: var(--brand-blue);
    font-weight: 600;
    white-space: nowrap;
  }
  .brand-mark__dot { display: block; border-radius: 50%; background: var(--brand-blue); flex: none; }
  .card--front .brand-mark { left: 0; right: 0; top: 124px; justify-content: center; font-size: 34px; }
  .card--front .brand-mark__dot { width: 32px; height: 32px; }
  .card--back .brand-mark { left: 34px; top: 34px; font-size: 28px; }
  .card--back .brand-mark__dot { width: 24px; height: 24px; }

  .contact { position: absolute; left: 50px; top: 112px; color: var(--ink); }
  .contact__name { color: var(--name-blue); font-weight: 600; font-size: 19px; line-height: 1.2; }
  .contact__role { font-size: 14px; margin-bottom: 16px; }
  .contact__address { font-size: 14px; line-height: 1.4; margin-bottom: 14px; }
  .contact__list { list-style: none; font-size: 14px; line-height: 1.5; }
  .contact__list li { display: flex; align-items: center; gap: 10px; }
  .contact__list svg { width: 12px; height: 12px; fill: var(--name-blue); flex: none; }

  .mascot-area {
    position: absolute; right: 0; top: 70px; width: 270px; height: 230px;
    background: linear-gradient(135deg, var(--fish-teal) 0%, var(--fish-blue) 55%, var(--accent-orange) 100%);
    border-radius: 90px 0 0 90px;
  }
</style>
</head>
<body>
  <section class="card card--front" aria-label="Business card front">
    <div class="brand-mark"><span class="brand-mark__dot"></span>Tall Cedar Technology</div>
  </section>

  <section class="card card--back" aria-label="Business card back">
    <div class="brand-mark"><span class="brand-mark__dot"></span>Tall Cedar Technology</div>

    <div class="contact">
      <p class="contact__name">Daniel Brooks</p>
      <p class="contact__role">Managing Director</p>
      <p class="contact__address">48 Harbor Lane, Suite 210<br>Riverton, OR 97402.</p>
      <ul class="contact__list">
        <li><svg viewBox="0 0 24 24"><path d="M6.6 10.8a15 15 0 0 0 6.6 6.6l2.2-2.2a1 1 0 0 1 1-.25 11.4 11.4 0 0 0 3.6.6 1 1 0 0 1 1 1V20a1 1 0 0 1-1 1A17 17 0 0 1 3 4a1 1 0 0 1 1-1h3.5a1 1 0 0 1 1 1c0 1.25.2 2.45.6 3.6a1 1 0 0 1-.25 1z"/></svg>044-987 654 321</li>
        <li><svg viewBox="0 0 24 24"><path d="M2 5h20v14H2z M2 5l10 8 10-8"/></svg>info@tallcedartech.com</li>
        <li><svg viewBox="0 0 24 24"><path d="M10 14a5 5 0 0 0 7 0l3-3a5 5 0 0 0-7-7l-1 1 1.5 1.5 1-1a3 3 0 0 1 4 4l-3 3a3 3 0 0 1-4 0zM14 10a5 5 0 0 0-7 0l-3 3a5 5 0 0 0 7 7l1-1-1.5-1.5-1 1a3 3 0 0 1-4-4l3-3a3 3 0 0 1 4 0z"/></svg>www.tallcedartech.com</li>
      </ul>
    </div>

    <div class="mascot-area" role="img" aria-label="Brand mascot illustration area in blue, teal and orange"></div>
  </section>
</body>
</html>
```